Updated DJ business Card showing other businesses

DJ Kestro offers professional mobile dj services including DJ. MC. Karaoke.
Silent Disco (will attach logo)
I also offer a 360 Photo Booth.

Contact info:
(555) 314-7720
lenny.corbitt@mailvane.net
Social Media @DJKestroBPZ

```html
<!DOCTYPE html>
<html lang="en">
<head>
<meta charset="utf-8">
<title>DJ Kestro Business Card</title>
<link rel="stylesheet" href="https://fonts.googleapis.com/css2?family=Anton&family=Lato:wght@400;700&family=Roboto+Condensed:ital,wght@0,700;1,700&display=swap">
<style>
  :root {
    --page: #2b2b2d;
    --card-black: #0a0a0a;
    --card-white: #ffffff;
    --brand-red: #d21f45;
    --ink: #111111;
    --muted-grey: #8a8a8a;
    --on-dark: #ffffff;
  }
  * { box-sizing: border-box; margin: 0; padding: 0; }
  html, body {
    width: 1200px; height: 900px; overflow: hidden;
    background: var(--page);
  }
  .sheet {
    position: relative; width: 1200px; height: 900px;
  }
  .card {
    position: absolute; left: 250px; width: 700px; height: 400px;
    border-radius: 28px; overflow: hidden;
  }
  /* Front card */
  .card--front {
    top: 35px; background: var(--card-black);
    display: flex; flex-direction: column; align-items: center; justify-content: center;
  }
  .front__logo {
    font-family: "Anton", sans-serif; font-size: 112px; line-height: 1;
    color: var(--on-dark); letter-spacing: 2px;
    display: flex; align-items: center; gap: 22px;
  }
  .front__logo-mark {
    width: 26px; height: 26px; background: var(--brand-red); border-radius: 50%;
  }
  .front__services {
    margin-top: 42px;
    font-family: "Roboto Condensed", sans-serif; font-weight: 700;
    font-size: 27px; color: var(--on-dark); letter-spacing: 1.5px;
  }
  .front__extra {
    margin-top: 6px;
    font-family: "Roboto Condensed", sans-serif; font-weight: 700; font-style: italic;
    font-size: 16px; color: var(--on-dark); letter-spacing: 1.5px;
  }
  /* Back card */
  .card--back {
    top: 465px; background: var(--card-white);
  }
  .back__art {
    position: absolute; left: 0; top: 0; width: 330px; height: 400px;
    background: linear-gradient(135deg, var(--brand-red) 0%, var(--brand-red) 38%, var(--ink) 62%, var(--ink) 100%);
  }
  .back__content {
    position: absolute; right: 40px; top: 34px; width: 330px;
    text-align: right;
  }
  .back__brand {
    font-family: "Anton", sans-serif; font-size: 22px; color: var(--brand-red);
    letter-spacing: 1px; line-height: 1;
  }
  .back__headline {
    font-family: "Anton", sans-serif; font-size: 27px; line-height: 1.12;
    color: var(--ink); letter-spacing: 0.5px; margin-top: 4px;
  }
  .back__services {
    font-family: "Lato", sans-serif; font-weight: 700; font-size: 25px;
    color: var(--brand-red); margin-top: 4px;
  }
  .back__partner {
    display: flex; justify-content: flex-end; margin-top: 6px;
  }
  .partner-badge {
    width: 76px; height: 36px; border-radius: 18px; background: var(--muted-grey);
  }
  .contact { margin-top: 12px; list-style: none; }
  .contact__item {
    display: flex; justify-content: flex-end; align-items: center; gap: 10px;
    font-family: "Lato", sans-serif; color: var(--ink);
    font-size: 16px; line-height: 1.55;
  }
  .contact__item--phone { font-size: 24px; font-weight: 700; }
  .contact__icon { width: 16px; height: 16px; flex: none; }
  .contact__social-dot {
    width: 14px; height: 14px; border-radius: 50%; background: var(--brand-red); flex: none;
  }
</style>
</head>
<body>
<main class="sheet">
  <section class="card card--front">
    <div class="front__logo"><span class="front__logo-mark"></span>DJ KESTRO</div>
    <p class="front__services">DJ | MC | KARAOKE | SILENT DISCO</p>
    <p class="front__extra">I ALSO OFFER A 360 PHOTO BOOTH.</p>
  </section>

  <section class="card card--back">
    <div class="back__art" role="img" aria-label="Large mascot illustration in black and white over a red field"></div>
    <div class="back__content">
      <p class="back__brand">DJ KESTRO</p>
      <h1 class="back__headline">OFFERS PROFESSIONAL MOBILE DJ SERVICES INCLUDING</h1>
      <p class="back__services">DJ | MC | Karaoke</p>
      <div class="back__partner"><span class="partner-badge" role="img" aria-label="Silent disco partner badge"></span></div>
      <ul class="contact">
        <li class="contact__item contact__item--phone">(555) 314-7720
          <svg class="contact__icon" viewBox="0 0 16 16"><path d="M3 1h3l1.5 4-2 1.5a9 9 0 0 0 4 4L11 8.5l4 1.5v3a2 2 0 0 1-2 2A12 12 0 0 1 1 3a2 2 0 0 1 2-2z" fill="var(--brand-red)"/></svg>
        </li>
        <li class="contact__item">lenny.corbitt@mailvane.net
          <svg class="contact__icon" viewBox="0 0 16 16"><rect x="1" y="3" width="14" height="10" rx="1" fill="var(--brand-red)"/><path d="M1.5 3.5 8 9l6.5-5.5" stroke="#fff" stroke-width="1.2" fill="none"/></svg>
        </li>
        <li class="contact__item">www.kestrosound.com
          <svg class="contact__icon" viewBox="0 0 16 16"><circle cx="8" cy="8" r="7" fill="var(--brand-red)"/><path d="M1 8h14M8 1c-3 3.5-3 10.5 0 14M8 1c3 3.5 3 10.5 0 14" stroke="#fff" stroke-width="1" fill="none"/></svg>
        </li>
        <li class="contact__item" style="font-size:20px;font-weight:700;"><span class="contact__social-dot"></span>@DJKestroBPZ</li>
      </ul>
    </div>
  </section>
</main>
</body>
</html>
```